Update Old OR create new Website

Current Website is looking a bit old, I did this one a few years back.

Would like a fresh new look, current website sitepress theme is " the Vanta theme" from plumcrate and I just purchased this theme - "bravlo" also from plumcrate, I quite like the look of - http://bravlo.quorvex-skins.com/tech-business/ and if we could get somthing simlar would be great.

current website is at http://www.hle.com.au, have been playing around with the slider that i like.

I have said 5 pages to be designed but really it is just a 5 page website where most pages will look the same.

Any questions please let me know

Target Market(s)

Business

Coding

Coded - Design and coding required

Number of Pages Required

5+ page

Font styles to use
Sans Serif

Colors
33a6d7
0292cd
ffffff
0255a3

Requirements
Must have
• Device compatibility - pc, tablet, phone
Nice to have
• video
Should not have
• vunerabilities. Must also use images that will expire or disappear, ie must be uploaded to site not links to elsewhere.

```html
<!DOCTYPE html>
<html lang="en">
<head>
<meta charset="utf-8">
<title>HLE Technologies</title>
<link rel="stylesheet" href="https://fonts.googleapis.com/css2?family=Anton&family=Lato:wght@400;700;900&display=swap">
<style>
  :root {
    --brand-blue: #33a6d7;
    --brand-deep: #0292cd;
    --white: #ffffff;
    --nav-grey: #6b6b6b;
    --ink: #222222;
    --headline: #585858;
    --panel: rgba(215, 215, 215, 0.72);
    --panel-edge: rgba(160, 160, 160, 0.55);
  }
  * { margin: 0; padding: 0; box-sizing: border-box; }
  html, body { width: 1200px; height: 579px; overflow: hidden; background: var(--white); }
  body { position: relative; font-family: "Lato", sans-serif; }

  .topbar {
    position: absolute; left: 0; top: 0; width: 1200px; height: 18px;
    background: var(--brand-blue); color: var(--white);
    font-size: 10.5px; letter-spacing: 0.3px;
  }
  .topbar-item { position: absolute; top: 3px; display: flex; align-items: center; gap: 4px; line-height: 12px; }
  .topbar-item svg { width: 9px; height: 9px; fill: var(--white); }
  .social-slot { position: absolute; top: 4px; width: 10px; height: 10px; background: var(--white); border-radius: 1px; }

  .site-header { position: absolute; left: 0; top: 18px; width: 1200px; height: 104px; background: var(--white); }
  .brand { position: absolute; left: 78px; top: 35px; display: flex; align-items: center; gap: 8px; }
  .brand-mark { width: 26px; height: 26px; background: var(--brand-blue); }
  .brand-name { font-size: 22px; font-weight: 400; color: var(--ink); letter-spacing: -0.3px; }

  .main-nav { position: absolute; left: 393px; top: 41px; display: flex; gap: 21px; }
  .main-nav a {
    font-size: 12px; font-weight: 900; color: var(--nav-grey);
    text-decoration: none; letter-spacing: 0.9px; text-transform: uppercase;
  }
  .search-toggle { position: absolute; left: 1014px; top: 41px; width: 13px; height: 13px; }

  .hero {
    position: absolute; left: 0; top: 122px; width: 1200px; height: 457px;
    background:
      radial-gradient(ellipse 260px 340px at 600px 200px, #8d8d8d 0%, rgba(120,120,120,0) 100%),
      linear-gradient(90deg, #3a3a3a 0%, #6a6a6a 22%, #7c7c7c 40%, #8a8a8a 50%, #7c7c7c 60%, #6a6a6a 78%, #3a3a3a 100%);
  }
  .hero-panel {
    position: absolute; left: 410px; top: 151px; width: 392px; height: 211px;
    background: var(--panel); border: 6px solid var(--panel-edge); border-radius: 3px;
    display: flex; flex-direction: column; align-items: center; justify-content: center;
    font-family: "Anton", sans-serif; color: var(--headline); text-transform: uppercase;
  }
  .headline-line { line-height: 37px; letter-spacing: 2px; white-space: nowrap; }
  .headline-line .lead { font-size: 29px; letter-spacing: 3px; }
  .headline-line .joiner { font-size: 17px; letter-spacing: 1px; }
  .headline-line .mark { font-size: 36px; color: #3c3c3c; }

  .scroll-cue { position: absolute; left: 586px; top: 396px; width: 32px; height: 32px; }
</style>
</head>
<body>
  <div class="topbar">
    <div class="topbar-item" style="left:62px">
      <svg viewBox="0 0 10 10"><path d="M5 0a3.4 3.4 0 0 0-3.4 3.4C1.6 6 5 10 5 10s3.4-4 3.4-6.6A3.4 3.4 0 0 0 5 0zm0 4.8a1.4 1.4 0 1 1 0-2.8 1.4 1.4 0 0 1 0 2.8z"/></svg>
      <span>4b 2170 Harlow Rd, Upper Mt Crestwood</span>
    </div>
    <div class="topbar-item" style="left:296px">
      <svg viewBox="0 0 10 10"><path d="M2 0.5l1.8 2.1-1 1.2a6 6 0 0 0 3.4 3.4l1.2-1 2.1 1.8-1 1.5C4.5 9.3 0.7 5.5 0.5 1.5z"/></svg>
      <span>1300 555 014</span>
    </div>
    <div class="topbar-item" style="left:417px">
      <svg viewBox="0 0 10 10"><path d="M0 2h10v0.8L5 5.8 0 2.8zM0 4l5 3 5-3v4.5H0z"/></svg>
      <span>info@hle.com.au</span>
    </div>
    <span class="social-slot" style="left:913px"></span>
    <span class="social-slot" style="left:958px"></span>
    <span class="social-slot" style="left:1004px"></span>
  </div>

  <header class="site-header">
    <div class="brand">
      <span class="brand-mark"></span>
      <span class="brand-name">HLE Technologies</span>
    </div>
    <nav class="main-nav">
      <a href="#">Home</a>
      <a href="#">Servers</a>
      <a href="#">Networks</a>
      <a href="#">Managed IT</a>
      <a href="#">Web</a>
      <a href="#">App's</a>
      <a href="#">Internet</a>
      <a href="#">Contact</a>
    </nav>
    <svg class="search-toggle" viewBox="0 0 14 14" aria-label="Search">
      <circle cx="5.8" cy="5.8" r="4.3" fill="none" stroke="#7a7a7a" stroke-width="2"/>
      <line x1="9" y1="9" x2="13" y2="13" stroke="#7a7a7a" stroke-width="2.2" stroke-linecap="round"/>
    </svg>
  </header>

  <section class="hero" role="img" aria-label="Grey-toned photo of a data centre corridor lined with server racks">
    <div class="hero-panel">
      <div class="headline-line"><span class="lead">What</span> <span class="joiner">would it take for your</span></div>
      <div class="headline-line"><span class="lead">Information Systems</span> <span class="joiner">to</span></div>
      <div class="headline-line"><span class="joiner">actually</span> <span class="lead">Improve</span> <span class="joiner">the</span></div>
      <div class="headline-line"><span class="lead">Performance</span> <span class="joiner">of your</span></div>
      <div class="headline-line"><span class="lead">Organisation</span><span class="mark">?</span></div>
    </div>
    <svg class="scroll-cue" viewBox="0 0 32 32" aria-label="Scroll down">
      <circle cx="16" cy="16" r="14.5" fill="none" stroke="#e6e6e6" stroke-width="1.6"/>
      <circle cx="16" cy="16" r="11" fill="#f0f0f0"/>
      <polyline points="10.5,13.5 16,19 21.5,13.5" fill="none" stroke="#7a7a7a" stroke-width="3" stroke-linecap="round" stroke-linejoin="round"/>
    </svg>
  </section>
</body>
</html>
```